Water Bottle Design

We are launching a water bottle and need a impactful design.

Target Market(s)

health conscious hipsters

Font styles to use
Sans Serif

Requirements
Must have
• Please include the logo (included) on one side of the bottle and these words on the other side of the bottle. "It’s simple, REUSE this bottle every day. Your action, will REDUCE the amount of waste produced. SAVE your body from drinking the harmful contaminants in your water from Non-BPA plastics. HELP someone else because proceeds from your purchase will help homeless veterans.
• We’re just two dudes that like to drink water and help people. #RefillForward"
• Use a total of two colors
• UPDATE: You do not have to use the bottle on the logo.
Nice to have
• The bottle itself is 34 ounces and looks like a normal water bottle. I will include the image in the files. We would need to be able to change the colors easily.
Should not have
• Do not use more than two colors. Colors should not be important to the design at this point.

```html
<!DOCTYPE html>
<html lang="en">
<head>
<meta charset="utf-8">
<title>Refill Forward – Bottle Wrap Colourways</title>
<link rel="stylesheet" href="https://fonts.googleapis.com/css2?family=Oswald:wght@300&family=Roboto+Condensed:wght@300;700&display=swap">
<style>
  :root {
    --page: #ffffff;
    --ink-light: #ffffff;
    --green-base: #7cc63e;
    --green-deep: #1e6b1f;
    --blue-base: #1e8fd8;
    --blue-deep: #15137c;
  }
  * { box-sizing: border-box; margin: 0; padding: 0; }
  html, body {
    width: 784px; height: 1200px; overflow: hidden;
    background: var(--page);
  }
  .canvas { position: relative; width: 784px; height: 1200px; }

  .wrap {
    position: absolute; top: 160px; width: 292px; height: 880px;
    border-radius: 28px;
    background: var(--base);
  }
  .wrap--green { left: 44px; --base: var(--green-base); --deep: var(--green-deep); }
  .wrap--blue  { left: 444px; --base: var(--blue-base); --deep: var(--blue-deep); }

  .salute-figure {
    position: absolute; left: 52px; top: 244px; width: 188px; height: 252px;
    background: var(--deep);
    border-radius: 60px 60px 0 0;
  }
  .rule {
    position: absolute; left: 26px; top: 496px; width: 242px; height: 3px;
    background: var(--deep);
  }
  .hashtag {
    position: absolute; left: 39px; top: 502px;
    font-family: "Oswald", sans-serif; font-weight: 300;
    font-size: 48px; letter-spacing: -1px;
    color: var(--deep);
  }
  .headline {
    position: absolute; left: 39px; top: 582px; width: 250px;
    font-family: "Roboto Condensed", sans-serif; font-weight: 700;
    font-size: 25px; line-height: 29px; letter-spacing: -0.3px;
    color: var(--ink-light);
  }
  .manifesto {
    position: absolute; left: 39px; top: 676px; width: 229px;
    font-family: "Roboto Condensed", sans-serif; font-weight: 300;
    font-size: 10.6px; line-height: 17px; text-align: justify;
    color: var(--ink-light);
  }
  .brand {
    position: absolute; left: 74px; top: 808px;
    display: flex; align-items: center; gap: 8px;
  }
  .brand-mark { width: 14px; height: 14px; background: var(--deep); }
  .brand-name {
    font-family: "Oswald", sans-serif; font-weight: 300;
    font-size: 24px; color: var(--deep);
  }
</style>
</head>
<body>
<main class="canvas">
  <section class="wrap wrap--green">
    <div class="salute-figure" role="img" aria-label="Silhouette of a saluting soldier"></div>
    <div class="rule"></div>
    <p class="hashtag">#RefillForward</p>
    <h1 class="headline">We’re just two dudes that like to drink water and help people.</h1>
    <p class="manifesto">It’s simple, REUSE this bottle every day. Your action, will REDUCE the amount of waste produced. SAVE your body from drinking the harmful contaminants in your water from Non-BPA plastics. HELP someone else because proceeds from your purchase will help homeless veterans.</p>
    <div class="brand"><span class="brand-mark"></span><span class="brand-name">Refill Forward</span></div>
  </section>

  <section class="wrap wrap--blue">
    <div class="salute-figure" role="img" aria-label="Silhouette of a saluting soldier"></div>
    <div class="rule"></div>
    <p class="hashtag">#RefillForward</p>
    <h1 class="headline">We’re just two dudes that like to drink water and help people.</h1>
    <p class="manifesto">It’s simple, REUSE this bottle every day. Your action, will REDUCE the amount of waste produced. SAVE your body from drinking the harmful contaminants in your water from Non-BPA plastics. HELP someone else because proceeds from your purchase will help homeless veterans.</p>
    <div class="brand"><span class="brand-mark"></span><span class="brand-name">Refill Forward</span></div>
  </section>
</main>
</body>
</html>
```